Real estate company needs a card that makes you say WOW!

We need an awesome business card for our real estate company, Stonebrook Realty Partners of Chicago, that will stand out from the crowd. We specialize in buying and selling real estate, property management, and real estate investments (Flips & Rentals). On the business card, I need the following:

- Our logo
- Services
- My name & contact info (Derek Ollanby, 630-517-2946, Derek@StonebrookRPC.com)
- My title (Director of Acquisitions)
- StonebrookRPC.com

I attached an EPS file of our logo. Let me know if you have any questions. Thank you in advance!

```html
<!DOCTYPE html>
<html lang="en">
<head>
<meta charset="UTF-8">
<title>Stonebrook Realty Partners of Chicago – Business Card</title>
<link href="https://fonts.googleapis.com/css2?family=Marcellus&family=Bitter:wght@400&display=swap" rel="stylesheet">
<style>
  :root {
    --bg: #e9e7e4;
    --card: #ffffff;
    --brand-blue: #1f6db3;
    --ink: #3a3a3c;
    --muted: #6d6e71;
    --rule: #4a4a4c;
  }
  * { box-sizing: border-box; margin: 0; padding: 0; }
  html, body { width: 1200px; height: 455px; overflow: hidden; }
  body {
    background: var(--bg);
    position: relative;
    font-family: "Bitter", Georgia, serif;
    color: var(--ink);
  }
  .card {
    position: absolute;
    top: 72px;
    width: 530px;
    height: 310px;
    background: var(--card);
    box-shadow: 0 2px 10px rgba(0,0,0,0.18);
  }
  .card--front { left: 50px; }
  .card--back { left: 620px; }

  .brand-name {
    font-family: "Marcellus", Georgia, serif;
    font-weight: 400;
    color: var(--brand-blue);
    text-align: center;
    line-height: 1.15;
  }
  .card--front .brand-name {
    position: absolute;
    top: 52px;
    left: 0;
    width: 100%;
    font-size: 34px;
    letter-spacing: 1px;
  }
  .card--back .brand-name {
    position: absolute;
    top: 96px;
    left: 30px;
    width: 230px;
    font-size: 25px;
    letter-spacing: 0.5px;
  }

  /* Front: person + contact */
  .person {
    position: absolute;
    top: 205px;
    right: 290px;
    text-align: right;
  }
  .person__name {
    font-family: "Marcellus", Georgia, serif;
    font-size: 22px;
    color: var(--brand-blue);
  }
  .person__title {
    font-family: "Bitter", Georgia, serif;
    font-size: 12px;
    color: var(--ink);
    margin-top: 2px;
  }
  .divider {
    position: absolute;
    left: 252px;
    top: 190px;
    width: 2px;
    height: 72px;
    background: var(--rule);
  }
  .contact {
    position: absolute;
    left: 266px;
    top: 188px;
    list-style: none;
    font-family: "Bitter", Georgia, serif;
    font-size: 14px;
    color: var(--ink);
  }
  .contact li {
    display: flex;
    align-items: center;
    gap: 6px;
    height: 24px;
  }
  .contact svg { width: 13px; height: 13px; fill: var(--ink); flex: none; }

  /* Back: services + web */
  .services {
    position: absolute;
    left: 300px;
    top: 56px;
  }
  .services__heading {
    font-size: 13px;
    color: #222;
    margin-bottom: 12px;
  }
  .services__list { list-style: none; font-size: 13px; color: var(--ink); }
  .services__list li {
    margin-bottom: 13px;
    padding-left: 6px;
  }
  .services__list li::before { content: "\2022"; margin-right: 6px; }
  .services__list li:nth-child(2) { margin-left: 6px; }
  .services__list li:nth-child(3) { margin-left: 12px; }

  .web {
    position: absolute;
    left: 0;
    width: 100%;
    top: 238px;
    text-align: center;
    font-size: 19px;
    color: #2b2b2d;
    letter-spacing: 0.3px;
  }
  .web__name { color: var(--brand-blue); }
</style>
</head>
<body>
  <section class="card card--front" aria-label="Business card front">
    <div class="brand-name">Stonebrook Realty Partners<br>of Chicago</div>

    <div class="person">
      <div class="person__name">Derek Ollanby</div>
      <div class="person__title">Director of Acquisitions</div>
    </div>
    <div class="divider"></div>
    <ul class="contact">
      <li>
        <svg viewBox="0 0 16 16" aria-hidden="true"><path d="M8 0a8 8 0 1 0 0 16A8 8 0 0 0 8 0zm0 1.5a6.5 6.5 0 1 1 0 13 6.5 6.5 0 0 1 0-13zM5.6 4l1.3 2.2-.8.8c.5 1.2 1.4 2.1 2.6 2.6l.8-.8L11.7 10l-.9 1.4C8 11.2 4.8 8 4.6 5.2z"/></svg>
        630-517-2946
      </li>
      <li>
        <svg viewBox="0 0 16 16" aria-hidden="true"><path d="M1 3h14v10H1zm1.5 1.5v.3L8 9l5.5-4.2v-.3zm0 2.2v4.8h11V6.7L8 10.9z"/></svg>
        Derek@StonebrookRPC.com
      </li>
      <li>
        <svg viewBox="0 0 16 16" aria-hidden="true"><path d="M8 0a8 8 0 1 0 0 16A8 8 0 0 0 8 0zm-1 1.6v3.2H4.6A6.5 6.5 0 0 1 7 1.6zm2 0a6.5 6.5 0 0 1 2.4 3.2H9zM3.9 6.3H7v3.4H3.9a6.6 6.6 0 0 1 0-3.4zm5.1 0h3.1a6.6 6.6 0 0 1 0 3.4H9zm-4.4 4.9H7v3.2a6.5 6.5 0 0 1-2.4-3.2zm4.4 0h2.4A6.5 6.5 0 0 1 9 14.4z"/></svg>
        www.StonebrookRPC.com
      </li>
    </ul>
  </section>

  <section class="card card--back" aria-label="Business card back">
    <div class="brand-name">Stonebrook Realty Partners of Chicago</div>

    <div class="services">
      <h2 class="services__heading">We Specialize In</h2>
      <ul class="services__list">
        <li>Buying &amp; Selling Real Estate</li>
        <li>Property Management</li>
        <li>Real Estate Investments</li>
      </ul>
    </div>

    <div class="web">www.<span class="web__name">Stonebrook</span>RPC.com</div>
  </section>
</body>
</html>
```